Door Hanger for Bright Harbor Painters

Design a double-sided door hanger that reinforces Bright Harbor Painters’ brand identity while promoting our interior painting services. This piece will be distributed in residential neighborhoods during the winter and should make a strong visual impression at a glance while offering enough detail to motivate follow-up. See attached design brief.

```html
<!DOCTYPE html>
<html lang="en">
<head>
<meta charset="utf-8">
<title>Bright Harbor Painters – Door Hanger</title>
<link href="https://fonts.googleapis.com/css2?family=Poppins:wght@400;500;600;700;800&display=swap" rel="stylesheet">
<style>
  :root{
    --stage:#a8acaa;
    --board:#262626;
    --board-light:#3a3a3a;
    --green:#8fc76b;
    --green-deep:#5e8f4c;
    --ink:#3a3a3a;
    --white:#ffffff;
  }
  *{box-sizing:border-box;margin:0;padding:0}
  html,body{width:1200px;height:2261px;overflow:hidden}
  body{background:var(--stage);font-family:"Poppins",sans-serif;position:relative}
  .hanger{position:absolute;top:500px;width:530px;height:1260px;overflow:hidden;
    background:radial-gradient(ellipse at 50% 45%,var(--board-light),var(--board) 70%);
    box-shadow:0 30px 40px rgba(0,0,0,.25)}
  .hanger--front{left:45px}
  .hanger--back{left:625px}
  .hanger > *{position:absolute}
  .die-guide,.hill{left:0;top:0;width:530px;height:1260px}
  .center{left:0;width:530px;text-align:center}
  .headline-interior{top:250px;font-size:70px;font-weight:800;color:var(--green);line-height:1}
  .headline-painting{top:318px;font-size:72px;font-weight:800;color:var(--white);line-height:1}
  .headline-services{top:388px;font-size:32px;font-weight:700;color:var(--white);letter-spacing:16px;padding-left:16px;line-height:1}
  .trust-badge{left:55px;top:442px;width:421px;height:90px;background:var(--green);border-radius:6px;
    display:flex;align-items:center;justify-content:center;text-align:center;
    font-size:37px;font-weight:800;color:var(--ink);line-height:.98}
  .since{top:540px;font-size:26px;font-weight:700;color:var(--white);letter-spacing:7px;padding-left:7px}
  .photo{width:150px;height:107px;border:2px solid #ddd}
  .photo--dining{background:linear-gradient(180deg,#4a4540,#8a6a4a 60%,#b07a48)}
  .photo--kitchen{background:linear-gradient(180deg,#e8e3dc,#9b6a48 60%,#c9b9a5)}
  .photo--hall{background:linear-gradient(180deg,#f0f0ea,#c8ccc0 60%,#7f8578)}
  .photo--stair{background:linear-gradient(180deg,#c7c1b8,#8a4a2e 55%,#e9e6e0)}
  .photo--ceiling{background:linear-gradient(180deg,#8a5a38,#e6dccb 55%,#d8b23a)}
  .photo--living{background:linear-gradient(180deg,#5a4a3c,#8fa0b0 50%,#6a5444)}
  .brand-name{color:var(--green-deep);font-weight:800;line-height:1}
  .brand-name--front{top:840px;font-size:50px}
  .brand-name--back{top:268px;font-size:46px;color:var(--white)}
  .tagline{left:53px;top:1033px;width:428px;height:58px;border-radius:10px;background:#2e2e2e;
    color:var(--white);font-size:19px;line-height:1.15;display:flex;align-items:center;justify-content:center;text-align:center}
  .contact{top:1103px;font-size:30px;font-weight:700;color:var(--ink);line-height:1}
  .contact-sub{top:1142px;font-size:17px;color:var(--ink);letter-spacing:8px;padding-left:8px;line-height:1}
  .web{top:1178px;font-size:37px;font-weight:700;color:var(--ink);line-height:1}
  .web span{color:var(--green-deep)}
  .about{top:400px;width:205px;color:var(--white);font-size:13px;line-height:15px}
  .about p+p{margin-top:15px}
  .about--left{left:53px;width:200px}
  .about--right{left:297px;width:210px}
  .service{width:140px;text-align:center;font-size:15px;font-weight:700;color:var(--ink);line-height:1.2}
  .service svg{display:block;margin:0 auto 4px}
  .divider{width:0;border-left:2px dashed #555;height:70px}
</style>
</head>
<body>

<section class="hanger hanger--front" aria-label="Door hanger front">
  <svg class="die-guide" viewBox="0 0 530 1260" fill="none" stroke="rgba(255,255,255,.18)" stroke-width="1.5">
    <rect x="12" y="12" width="506" height="1236"/>
    <path d="M14 190 L190 190 Q215 190 222 175 A60 60 0 1 1 308 175 Q315 190 340 190 L516 190"/>
    <circle cx="265" cy="140" r="75"/>
  </svg>
  <div class="center headline-interior">INTERIOR</div>
  <div class="center headline-painting">PAINTING</div>
  <div class="center headline-services">SERVICES</div>
  <div class="trust-badge">TRUSTED LOCAL<br>PROFESSIONALS</div>
  <div class="center since">SINCE 2005</div>
  <div class="photo photo--dining" style="left:30px;top:580px" role="img" aria-label="Photo of a freshly painted dining room"></div>
  <div class="photo photo--kitchen" style="left:189px;top:580px" role="img" aria-label="Photo of a painted kitchen and living area"></div>
  <div class="photo photo--hall" style="left:347px;top:580px" role="img" aria-label="Photo of a room being painted"></div>
  <svg class="hill" viewBox="0 0 530 1260">
    <path fill="#8fc76b" d="M245 722 Q270 700 305 716 L350 745 Q385 735 415 760 L530 845 L530 905 L385 795 Q360 775 330 795 Z"/>
    <path fill="#ffffff" d="M0 985 L170 722 Q190 698 212 712 L330 790 Q360 768 388 790 L530 900 L530 1260 L0 1260 Z"/>
  </svg>
  <div class="center brand-name brand-name--front">BRIGHT HARBOR<br>PAINTERS</div>
  <div class="tagline">Quality finishes, exceptional customer<br>service and reasonable rates</div>
  <div class="center contact">Contact Us Now</div>
  <div class="center contact-sub">For more information</div>
  <div class="center web">www.<span>bhpainters</span>.com</div>
</section>

<section class="hanger hanger--back" aria-label="Door hanger back">
  <svg class="die-guide" viewBox="0 0 530 1260" fill="none" stroke="rgba(255,255,255,.18)" stroke-width="1.5">
    <rect x="12" y="12" width="506" height="1236"/>
    <path d="M14 190 L190 190 Q215 190 222 175 A60 60 0 1 1 308 175 Q315 190 340 190 L516 190"/>
    <circle cx="265" cy="140" r="75"/>
  </svg>
  <div class="center brand-name brand-name--back">BRIGHT HARBOR<br>PAINTERS</div>
  <div class="about about--left">
    <p>Bright Harbor Painters provides a full range of interior painting services for Vermont homes and businesses, taking pride in our clean, communicative workmanship, and friendly, professional tradespeople.</p>
    <p>From walls and ceilings to trim and cabinets, our friendly team of professionals is ready to handle all aspects of your project with care and attention to detail.</p>
  </div>
  <div class="about about--right">
    <p>Proudly serving Vermont homes and businesses since 2005 with quality finishes, exceptional customer service and reasonable rates.</p>
    <p>We are access specialists and can safely complete difficult projects including vaulted ceilings, great rooms, foyers and stairways.</p>
    <p>Setting a higher standard for workmanship, client experience and value.</p>
  </div>
  <svg class="hill" viewBox="0 0 530 1260">
    <path fill="#8fc76b" d="M250 668 Q275 650 308 664 L360 708 Q395 698 420 718 L530 800 L530 848 L395 755 Q375 740 350 760 Z"/>
    <path fill="#ffffff" d="M0 815 L180 655 Q200 637 222 653 L350 760 Q378 740 400 760 L530 846 L530 1260 L0 1260 Z"/>
  </svg>

  <div class="service" style="left:26px;top:745px">
    <svg width="52" height="52" viewBox="0 0 52 52"><circle cx="26" cy="26" r="24" fill="#5e8f4c" stroke="#fff" stroke-width="2"/><rect x="16" y="14" width="18" height="10" fill="#fff"/><rect x="24" y="24" width="3" height="16" fill="#fff"/></svg>Walls</div>
  <div class="service" style="left:196px;top:745px">
    <svg width="52" height="52" viewBox="0 0 52 52"><circle cx="26" cy="26" r="24" fill="#5e8f4c" stroke="#fff" stroke-width="2"/><rect x="19" y="12" width="14" height="27" fill="none" stroke="#fff" stroke-width="3"/></svg>Trim &amp; Doors</div>
  <div class="service" style="left:358px;top:745px">
    <svg width="52" height="52" viewBox="0 0 52 52"><circle cx="26" cy="26" r="24" fill="#5e8f4c" stroke="#fff" stroke-width="2"/><rect x="13" y="16" width="26" height="5" fill="#fff"/><path d="M26 21 V36 M18 36 H34" stroke="#fff" stroke-width="3"/></svg>Ceilings</div>
  <div class="divider" style="left:170px;top:750px"></div>
  <div class="divider" style="left:362px;top:750px"></div>

  <div class="service" style="left:30px;top:845px">
    <svg width="52" height="52" viewBox="0 0 52 52"><circle cx="26" cy="26" r="24" fill="#5e8f4c" stroke="#fff" stroke-width="2"/><rect x="15" y="15" width="22" height="22" fill="none" stroke="#fff" stroke-width="2.5"/><path d="M26 15 V37 M15 26 H37" stroke="#fff" stroke-width="2.5"/></svg>Kitchens<br>&amp; Cabinets</div>
  <div class="service" style="left:196px;top:845px">
    <svg width="52" height="52" viewBox="0 0 52 52"><circle cx="26" cy="26" r="24" fill="#5e8f4c" stroke="#fff" stroke-width="2"/><path d="M16 38 H24 V32 H30 V26 H36 V38" fill="none" stroke="#fff" stroke-width="3"/></svg>High Access<br>or Stairways</div>
  <div class="service" style="left:358px;top:845px">
    <svg width="52" height="52" viewBox="0 0 52 52"><circle cx="26" cy="26" r="24" fill="#5e8f4c" stroke="#fff" stroke-width="2"/><rect x="18" y="13" width="16" height="26" fill="none" stroke="#fff" stroke-width="2.5"/><path d="M18 13 L34 26 L18 39 M34 13 L18 26 L34 39" stroke="#fff" stroke-width="1.8" fill="none"/></svg>Drywall<br>Repair</div>
  <div class="divider" style="left:170px;top:850px"></div>
  <div class="divider" style="left:362px;top:850px"></div>

  <div class="photo photo--stair" style="left:26px;top:983px" role="img" aria-label="Photo of a painted spiral stairway"></div>
  <div class="photo photo--ceiling" style="left:187px;top:983px" role="img" aria-label="Photo of scaffolding under a vaulted ceiling"></div>
  <div class="photo photo--living" style="left:348px;top:983px" role="img" aria-label="Photo of a finished great room"></div>
  <div class="center contact">Contact Us Now</div>
  <div class="center contact-sub">For more information</div>
  <div class="center web">www.<span>bhpainters</span>.com</div>
</section>

</body>
</html>
```